ORVET - Helping People with Disabilities

ORVET is a nonprofit that strives to enable people with physical disabilities to live meaningful, quality lives. ORVET needs a professional attractive website that:
• establishes a strong brand image
• presents Orvet's services to those who need it
• raises funds from potential donors
Please see WORD DOC attached for more information about design vision.

Target Market(s)

people with disabilities

Industry/Entity Type

charity website

Number of Pages Required

2 page

Font styles to use
Sans Serif

Requirements
Must have
• 1. 2 pages means 1 design for homepage and 1 design for top of inner pages (banner ideas)
Nice to have
• please see attached design brief (WORD DOC)

```html
<!DOCTYPE html>
<html lang="en">
<head>
<meta charset="utf-8">
<title>ORVET – Helping People with Disabilities</title>
<link href="https://fonts.googleapis.com/css2?family=Lato:wght@400;700;900&family=Roboto:wght@400;500;700&display=swap" rel="stylesheet">
<style>
:root{
  --green:#15774a;
  --green-dark:#126b41;
  --white:#ffffff;
  --ink:#1d1d1d;
  --navy:#15335a;
  --about-bg:#efefec;
  --edu-bg:#f1f0ed;
  --cards-bg:#e5e4e0;
  --rule:#c9c9c9;
}
*{box-sizing:border-box;margin:0;padding:0}
html,body{width:1200px;height:3074px;overflow:hidden}
body{position:relative;font-family:'Lato',sans-serif;color:var(--ink);background:var(--white)}
.abs{position:absolute}

.topbar{left:0;top:0;width:1200px;height:40px;background:var(--green)}
.social{position:absolute;top:12px;display:flex;gap:14px;left:106px}
.social span{width:16px;height:16px;border-radius:50%;background:var(--white);display:block}

.header{left:0;top:40px;width:1200px;height:143px;background:var(--white)}
.logo{position:absolute;left:105px;top:40px;font-family:'Roboto',sans-serif;font-weight:700;font-size:44px;color:var(--green);letter-spacing:1px}
.nav{position:absolute;top:58px;left:0;width:1200px;font-size:13px;color:var(--navy)}
.nav a{position:absolute;text-decoration:none;color:var(--navy);top:0;height:26px;line-height:26px}
.nav .active{background:var(--green);color:var(--white);padding:0 16px}

.hero{left:0;top:183px;width:1200px;height:467px;background:linear-gradient(180deg,#2f8a5a 0%,#2b8454 45%,#2f8656 100%)}
.hero-title{position:absolute;left:0;top:145px;width:1200px;text-align:center;font-family:'Roboto',sans-serif;font-weight:700;font-size:46px;line-height:56px;color:var(--white)}
.hero-actions{position:absolute;top:337px;left:0;width:1200px;display:flex;justify-content:center;gap:16px;font-size:13px;color:var(--white);font-family:'Roboto',sans-serif}
.hero-actions span{height:20px;line-height:18px;padding:0 8px}
.hero-actions .outline{border:1px solid var(--white)}

.ticker{left:0;top:650px;width:1200px;height:105px;background:var(--white);text-align:center;line-height:105px;font-family:'Roboto',sans-serif;font-weight:700;font-size:20px;color:var(--green)}
.ticker-rule{left:0;top:755px;width:1200px;height:7px;background:var(--rule)}

.about{left:0;top:762px;width:1200px;height:837px;background:var(--about-bg)}
.about h2{position:absolute;left:108px;top:118px;font-family:'Lato',sans-serif;font-weight:700;font-size:40px;color:var(--green)}
.about-copy{position:absolute;left:617px;top:115px;border-left:2px solid var(--green);padding:8px 0 0 12px;width:455px;font-size:14.6px;line-height:22.6px;color:#2a2a2a}
.btn-solid{position:absolute;left:629px;top:232px;height:27px;line-height:27px;padding:0 10px;background:var(--green);color:var(--white);font-size:13px}
.video-back{position:absolute;left:203px;top:392px;width:781px;height:384px;background:var(--green)}
.video{position:absolute;left:225px;top:348px;width:774px;height:405px;background:linear-gradient(135deg,#3c3d46 0%,#6a5232 35%,#c9911f 60%,#4b6e86 100%)}
.video svg{position:absolute;left:0;top:0}

.edu{left:0;top:1599px;width:1200px;height:841px;background:var(--edu-bg)}
.photo{position:absolute;border:3px solid var(--green);background:linear-gradient(180deg,#3a4a6a 0%,#8e6a56 40%,#c9a37e 70%,#d8c2a6 100%)}
.edu-text{position:absolute;font-family:'Roboto',sans-serif;color:var(--navy)}
.edu-text h3{font-size:39px;font-weight:700;color:var(--green);line-height:44px}
.edu-text p{font-size:19px;line-height:30px}

.cards{left:0;top:2440px;width:1200px;height:634px;background:var(--cards-bg)}
.card{position:absolute;top:152px;width:339px;text-align:center}
.card .thumb{position:relative;width:339px;height:200px;border:3px solid var(--green);background:linear-gradient(135deg,#3c3d46 0%,#6a5232 35%,#c9911f 60%,#4b6e86 100%)}
.card h4{margin-top:20px;font-family:'Roboto',sans-serif;font-weight:700;font-size:20px;line-height:28px;color:#111}
.card p{margin-top:10px;font-family:'Roboto',sans-serif;font-size:12.5px;line-height:20px;color:#222}
.card .btn-ghost{display:inline-block;margin-top:22px;height:27px;line-height:25px;padding:0 8px;border:1px solid var(--green);font-family:'Roboto',sans-serif;font-size:13px;color:#111}
</style>
</head>
<body>

<div class="abs topbar">
  <div class="social" aria-label="Social links"><span></span><span></span><span></span><span></span><span></span></div>
</div>

<header class="abs header">
  <div class="logo">ORVET</div>
  <nav class="nav">
    <a style="left:855px">About Us</a>
    <a class="active" style="left:935px">Services</a>
    <a style="left:1042px">Contact</a>
  </nav>
</header>

<section class="abs hero" role="img" aria-label="Group of volunteers in green shirts walking outdoors with a wheelchair user, under a green overlay">
  <h1 class="hero-title">A good life for everyone,<br>like everyone</h1>
  <div class="hero-actions"><span>Get Involved</span><span class="outline">Donate</span></div>
</section>

<div class="abs ticker">News Scroll Ticket</div>
<div class="abs ticker-rule"></div>

<section class="abs about">
  <h2>About Us</h2>
  <p class="about-copy">Our future community is a vibrant and inclusive neighborhood designed with the needs and preferences of modern home buyers in mind. With its prime location and thoughtful amenities, it offers the perfect blend of comfort, convenience, and community.</p>
  <div class="btn-solid">Sign upfor Updates</div>
  <div class="video-back"></div>
  <div class="video" role="img" aria-label="Video still of a smiling young woman in a yellow sweater holding a green folder">
    <svg width="774" height="405" viewBox="0 0 774 405">
      <circle cx="387" cy="203" r="46" fill="#ffffff" fill-opacity="0.25"/>
      <path d="M372 180 L408 203 L372 226 Z" fill="#fff"/>
      <rect x="14" y="377" width="746" height="3" fill="#ffffff" fill-opacity="0.4"/>
      <rect x="14" y="377" width="80" height="3" fill="#fff"/>
      <circle cx="94" cy="378" r="4" fill="#fff"/>
      <path d="M24 388 L33 394 L24 400 Z" fill="#fff"/>
      <rect x="58" y="388" width="3" height="12" fill="#fff"/><rect x="64" y="388" width="3" height="12" fill="#fff"/>
      <rect x="94" y="389" width="10" height="10" fill="#fff"/>
      <path d="M145 388 L153 394 L145 400 Z" fill="#fff"/><rect x="154" y="388" width="2" height="12" fill="#fff"/>
      <path d="M195 391 H199 L204 387 V401 L199 397 H195 Z" fill="#fff"/>
      <text x="595" y="399" font-family="Roboto, sans-serif" font-size="12" fill="#fff">01:45 / 10:00</text>
      <circle cx="690" cy="394" r="6" fill="none" stroke="#fff" stroke-width="3"/>
      <rect x="727" y="388" width="16" height="12" fill="none" stroke="#fff" stroke-width="2"/>
    </svg>
  </div>
</section>

<section class="abs edu">
  <div class="edu-text" style="left:185px;top:175px">
    <h3>EDUCATION</h3>
    <p>Orvet works to impart education and<br>knowledge to people with disabilities<br>and<br>operates the dedicated campus</p>
  </div>
  <div class="photo" role="img" aria-label="Child in a wheelchair with a team mascot on a basketball court" style="left:632px;top:75px;width:463px;height:297px"></div>
  <div class="photo" role="img" aria-label="Child in a wheelchair with a team mascot on a basketball court" style="left:105px;top:424px;width:463px;height:297px"></div>
  <div class="edu-text" style="left:632px;top:502px">
    <h3>EDUCATION</h3>
    <p>Orvet works to impart education and<br>knowledge to people with disabilities<br>and<br>operates the dedicated campus</p>
  </div>
</section>

<section class="abs cards">
  <article class="card" style="left:44px">
    <div class="thumb" role="img" aria-label="Video still of a smiling young woman in a yellow sweater">
      <svg width="333" height="194" viewBox="0 0 333 194" style="position:absolute;left:0;top:0"><circle cx="166" cy="94" r="20" fill="#fff" fill-opacity="0.25"/><path d="M160 84 L176 94 L160 104 Z" fill="#fff"/><rect x="6" y="180" width="320" height="2" fill="#fff" fill-opacity="0.5"/></svg>
    </div>
    <h4>Building a community through<br>adaptive sports programs</h4>
    <p>ORVET offers a range of services to help individuals with<br>physical disabilities live fulfilling lives.</p>
    <span class="btn-ghost">Learn More</span>
  </article>
  <article class="card" style="left:434px">
    <div class="thumb" role="img" aria-label="Video still of a smiling young woman in a yellow sweater">
      <svg width="333" height="194" viewBox="0 0 333 194" style="position:absolute;left:0;top:0"><circle cx="166" cy="94" r="20" fill="#fff" fill-opacity="0.25"/><path d="M160 84 L176 94 L160 104 Z" fill="#fff"/><rect x="6" y="180" width="320" height="2" fill="#fff" fill-opacity="0.5"/></svg>
    </div>
    <h4>Building a community through<br>adaptive sports programs</h4>
    <p>ORVET offers a range of services to help individuals with<br>physical disabilities live fulfilling lives.</p>
    <span class="btn-ghost">Learn More</span>
  </article>
  <article class="card" style="left:824px">
    <div class="thumb" role="img" aria-label="Video still of a smiling young woman in a yellow sweater">
      <svg width="333" height="194" viewBox="0 0 333 194" style="position:absolute;left:0;top:0"><circle cx="166" cy="94" r="20" fill="#fff" fill-opacity="0.25"/><path d="M160 84 L176 94 L160 104 Z" fill="#fff"/><rect x="6" y="180" width="320" height="2" fill="#fff" fill-opacity="0.5"/></svg>
    </div>
    <h4>Building a community through<br>adaptive sports programs</h4>
    <p>ORVET offers a range of services to help individuals with<br>physical disabilities live fulfilling lives.</p>
    <span class="btn-ghost">Learn More</span>
  </article>
</section>

</body>
</html>
```